40k Ultra High Pressure Waterblasing Ad

We need 1 page flyer ad for our industry's brochure/membership directory.
We're a manufacturer & supplier for the Ultra High Pressure Waterblasting industry.
We'd like the ad to be simple and clean, highlighting some of our parts. Our dedication to our customers and affordable prices.
Some of the parts are Dorvel Mastrick Hoses, Sapphire Nozzles, Rotating Jetlance.

Our website is torvaflux.com

Requirements
Must have
• Dorvel Mastrick 40k Hose
• Sapphire Nozzles
• Rotating Jetlance
• **Update - Would like to incorporate the "iron skein logo w/ bulldog" from uploaded dorvel iron skein hose attachment. Highlighting the hose's features.
Nice to have
• Brief Bullet points or something else highlighting what we sell.
• - Pump replacement parts
• - Sapphire Nozzles
• - Rotating Jetlance
• - Fittings and adapters
• - Safety Gear
• I've uploaded past ads we've used.
Should not have
• Lots of text area

```html
<!DOCTYPE html>
<html lang="en">
<head>
<meta charset="utf-8">
<title>Torvaflux Technologies – Waterjetting Products Flyer</title>
<link href="https://fonts.googleapis.com/css2?family=Open+Sans:ital,wght@0,300;0,400;0,600;0,700;1,700;1,800&display=swap" rel="stylesheet">
<style>
  :root {
    --navy: #232a66;
    --cyan: #1ca3e3;
    --sky: #4196d2;
    --stone: #dcdde2;
    --white: #ffffff;
    --page: #1b1b1f;
  }
  * { margin: 0; padding: 0; box-sizing: border-box; }
  html, body { width: 1200px; height: 1200px; overflow: hidden; background: var(--page); }
  body { font-family: "Open Sans", sans-serif; position: relative; }

  .flyer {
    position: absolute; left: 192px; top: 24px;
    width: 742px; height: 1048px;
    transform: scale(1.1); transform-origin: top left;
    background: var(--navy); overflow: hidden;
  }
  .contact-bar {
    position: absolute; top: 44px; left: 0; width: 100%;
    text-align: center; color: var(--white); font-size: 16.5px; letter-spacing: .1px;
  }
  .contact-bar .sep { margin: 0 18px; }

  .headline-bubble {
    position: absolute; left: 62px; top: 99px; width: 332px; height: 170px;
    background: var(--white);
  }
  .headline-bubble h1 {
    position: absolute; left: 26px; top: 20px;
    font-weight: 300; color: var(--navy); font-size: 44px; line-height: 40px; letter-spacing: -.5px;
  }
  .bubble-tail { position: absolute; left: 262px; top: 268px; }

  .offer { position: absolute; left: 440px; top: 98px; font-style: italic; font-weight: 800; }
  .offer .price { color: var(--cyan); font-size: 36px; line-height: 41px; }
  .offer .call { color: var(--white); font-size: 36px; line-height: 41px; margin-top: 8px; }

  .product-strip { position: absolute; top: 319px; left: 0; width: 100%; height: 181px; display: flex; }
  .product-photo { width: 247.33px; height: 100%; }
  .product-photo.nozzles { background: radial-gradient(ellipse at center, #a9a8a4 0%, var(--stone) 45%); }
  .product-photo.jetlance { background: radial-gradient(ellipse at center, #8d8f95 0%, var(--sky) 50%); }
  .product-photo.hose { background: radial-gradient(ellipse at center, #8f969f 0%, var(--stone) 50%); }

  .brand-strip {
    position: absolute; top: 500px; left: 0; width: 100%; height: 84px;
    background: var(--white); display: flex;
  }
  .brand { width: 247.33px; display: flex; align-items: center; justify-content: center; gap: 7px;
    color: var(--navy); font-weight: 700; font-size: 17px; letter-spacing: .5px; }
  .brand .dot { width: 10px; height: 10px; border-radius: 50%; background: var(--navy); }

  .features { position: absolute; top: 584px; left: 0; width: 100%; height: 264px; color: var(--white); }
  .features h2 { font-weight: 400; font-size: 17px; color: var(--cyan); position: absolute; }
  .features ul { list-style: none; position: absolute; font-size: 11px; line-height: 18px; }
  .features li::before { content: "•"; margin-right: 4px; }
  .two-col { display: grid; grid-template-columns: 143px 140px; }
  .hose-list li { padding-left: 9px; text-indent: -9px; }
  .hose-list li.gap { margin-top: 4px; }
  .hose-list li.sub { padding-left: 29px; }

  .closing { position: absolute; top: 848px; left: 0; width: 100%; height: 200px; background: var(--white); }
  .closing h2 {
    position: absolute; left: 84px; top: 24px;
    font-weight: 300; color: var(--navy); font-size: 48px; line-height: 45px; letter-spacing: -.3px;
  }
  .web-tag {
    position: absolute; left: 87px; top: 130px; width: 169px; height: 29px;
    background: var(--navy); color: var(--white); font-weight: 700; font-size: 14.5px;
    display: flex; align-items: center; justify-content: center;
  }
  .company-mark {
    position: absolute; left: 486px; top: 76px; display: flex; align-items: center; gap: 10px;
    color: var(--navy); font-weight: 700; font-size: 36px;
  }
  .company-mark .square { width: 18px; height: 18px; background: var(--cyan); }
</style>
</head>
<body>
  <main class="flyer">
    <p class="contact-bar">Torvaflux Technologies<span class="sep">|</span>Email: info@torvaflux.com<span class="sep">|</span>Ph: 555-014-2290</p>

    <div class="headline-bubble"><h1>QUALITY<br>WATERJETTING<br>PRODUCTS</h1></div>
    <svg class="bubble-tail" width="36" height="70" viewBox="0 0 36 70" aria-hidden="true">
      <polygon points="0,0 35,0 35,69" fill="#ffffff"/>
    </svg>

    <div class="offer">
      <p class="price">At Affordable<br>Prices</p>
      <p class="call">Call Now!<br>555-014-2290</p>
    </div>

    <section class="product-strip">
      <div class="product-photo nozzles" role="img" aria-label="Photo of sapphire nozzle fittings"></div>
      <div class="product-photo jetlance" role="img" aria-label="Photo of a rotating jetlance gun"></div>
      <div class="product-photo hose" role="img" aria-label="Photo of a coiled 40k high pressure hose"></div>
    </section>

    <section class="brand-strip">
      <div class="brand"><span class="dot"></span>Iron Skein</div>
      <div class="brand">Dorvel</div>
      <div class="brand">Shellguard</div>
    </section>

    <section class="features">
      <h2 style="left:54px;top:28px;">Pump Replacement Parts</h2>
      <ul class="two-col" style="left:54px;top:54px;">
        <li>Sapphire Nozzles</li><li>Fittings and adapters</li>
        <li>Rotating Jetlance</li><li>Safety Gear</li>
      </ul>

      <h2 style="left:52px;top:139px;">Dorvel Mastrick 40k Hose</h2>
      <ul class="two-col" style="left:55px;top:165px;">
        <li>Sapphire Nozzles</li><li>Rotating Jetlance</li>
      </ul>

      <h2 style="left:364px;top:28px;">IRONSKEIN Hose Features</h2>
      <ul class="hose-list" style="left:368px;top:54px;width:330px;">
        <li>IRONSKEIN abrasion resistant cover eliminates the obstructive PVC Cover</li>
        <li class="gap">Features HueAlertTM technology to provide early warning of hose wear</li>
        <li class="gap">Compact O.D&gt; reduces friction drag</li>
        <li class="gap" style="margin-top:11px;">Lighter weight assemblies (up to 16%)</li>
        <li class="sub">reduces Friction and drag</li>
        <li class="sub">reduces operator fatigue</li>
        <li class="sub">reduces freight costs</li>
      </ul>
    </section>

    <section class="closing">
      <h2>OUR CUSTOMERS<br>COME FIRST</h2>
      <p class="web-tag">www.torvaflux.com</p>
      <div class="company-mark"><span class="square"></span>Torvaflux</div>
    </section>
  </main>
</body>
</html>
```